retail package design for food snack

We need a full package design (front and back)for our retail food snack. It will be printed on a stand up zipper pouch. The snack is crunchy chilli. The the package will need to involve the logo, maybe a picture on the snack etc. we will require the back of the package including nutritional information, ingredients, company details, bar code and a QR code.
We have six flavours, so we would need to change the background colour and also the flavour name on the front (maybe in a circle) I've attached some photos of the product, the logo and what the package currently looks like. Its going to be printed on a stand-up pouch with a zipper lock (I've attached two package examples for reference only not design examples)

Requirements
Must have
• I envision the logo to be large on the package but happy to see all options

```html
<!DOCTYPE html>
<html lang="en">
<head>
<meta charset="utf-8">
<title>Auntie Ember – Extra Spicy pouch front</title>
<link rel="stylesheet" href="https://fonts.googleapis.com/css2?family=Arvo:wght@700&display=swap">
<style>
  :root {
    --stage: #e6e7e9;
    --red-deep: #b5121b;
    --red: #e0202a;
    --red-light: #ee3a3f;
    --silver: #d3d4d6;
    --charcoal: #3a3a3c;
    --maroon: #7a1419;
    --white: #ffffff;
    --snack-dark: #8e2a0e;
    --snack: #d0521c;
    --snack-light: #f08a2c;
  }
  * { box-sizing: border-box; margin: 0; padding: 0; }
  html, body {
    width: 1200px;
    height: 890px;
    overflow: hidden;
    background: var(--stage);
  }
  .canvas {
    position: relative;
    width: 1200px;
    height: 890px;
  }
  .pouch-front {
    position: absolute;
    left: 318px;
    top: 40px;
    width: 564px;
    height: 812px;
    box-shadow: 0 10px 24px rgba(0,0,0,0.25);
  }
  .pouch-front svg { display: block; width: 100%; height: 100%; }
  .brand-name,
  .tagline,
  .web-address,
  .flavour-name {
    font-family: "Arvo", Georgia, serif;
    font-weight: 700;
  }
</style>
</head>
<body>
<main class="canvas">
  <section class="pouch-front" aria-label="Auntie Ember crunchy chilli snacks, Extra Spicy, front of pouch">
    <svg viewBox="0 0 580 835" xmlns="http://www.w3.org/2000/svg">
      <defs>
        <linearGradient id="side-red" x1="0" y1="0" x2="1" y2="1">
          <stop offset="0" stop-color="var(--red-light)"/>
          <stop offset="0.45" stop-color="var(--red)"/>
          <stop offset="1" stop-color="var(--red-deep)"/>
        </linearGradient>
        <radialGradient id="snack-tones" cx="0.5" cy="0.35" r="0.7">
          <stop offset="0" stop-color="var(--snack-light)"/>
          <stop offset="0.55" stop-color="var(--snack)"/>
          <stop offset="1" stop-color="var(--snack-dark)"/>
        </radialGradient>
        <clipPath id="panel-clip"><rect width="580" height="835"/></clipPath>
        <path id="web-address-curve" d="M132 270 A158 158 0 0 0 448 270"/>
      </defs>

      <g clip-path="url(#panel-clip)">
        <!-- red side bands -->
        <rect class="side-band" width="580" height="835" fill="url(#side-red)" role="img" aria-label="Red faceted background pattern"/>

        <!-- central column: charcoal with silver arch over the badge -->
        <rect class="centre-column" x="120" y="0" width="340" height="835" fill="var(--charcoal)"/>
        <path class="silver-arch" d="M120 0 H460 V272 A170 170 0 0 1 120 272 Z" fill="var(--silver)"/>

        <!-- brand mark stand-in -->
        <circle class="brand-disc" cx="290" cy="270" r="136" fill="var(--maroon)"/>
        <text class="brand-name" x="290" y="268" text-anchor="middle" font-size="34" fill="var(--white)">Auntie Ember</text>
        <text class="tagline" x="290" y="304" text-anchor="middle" font-size="17" fill="var(--white)">crunchy chilli snacks</text>
        <text class="web-address" font-size="19" fill="var(--maroon)">
          <textPath href="#web-address-curve" startOffset="50%" text-anchor="middle">auntieember.com</textPath>
        </text>

        <!-- flavour -->
        <text class="flavour-name" x="290" y="500" text-anchor="middle" font-size="27" fill="var(--white)">Extra Spicy</text>

        <!-- snack photo window -->
        <circle class="photo-ring" cx="290" cy="822" r="276" fill="var(--white)"/>
        <circle class="snack-photo" cx="290" cy="822" r="266" fill="url(#snack-tones)" role="img" aria-label="Close-up photo of crunchy chilli snack"/>
      </g>
    </svg>
  </section>
</main>
</body>
</html>
```